We need to redo the www.tallowmere.com website. Content will be greatly reduced. TallowMere is a marketing consulting and marketing automation company that provides services to limousine and executive car service companies. Our main competitor's site is http://www.corvelquistpartners.com/, which I like very much. I would like tallowmere.com to have a similar format and a more simple user interface. We would need a home page, product page, services page, resource page, blog, about the company, and contact us page. Our colors are currently the green/blue of the logo, but we are happy to change colors and/or logo if a compelling design warranted - as a matter of fact, we are quite tired of the blue and green. :) I will fit content to design, but there are, you will see, a number of products and services that need to be covered. Again, I like the way the competitor arranged things so everything was easy to find. We want a wide width or "one page" format that uses a lot of images - we will purchase images as required.
Updates

We'd like the site to look more similar to the style of corvelquistpartners.com please :) Thank you!

Industry/Entity Type

Marketing

```html
<!DOCTYPE html>
<html lang="en">
<head>
<meta charset="utf-8">
<title>TallowMere – Marketing for Executive Car Services</title>
<link rel="stylesheet" href="https://fonts.googleapis.com/css2?family=Open+Sans:wght@300;400;600;700&display=swap">
<style>
  :root {
    --blue: #1d63b0;
    --blue-dark: #154c8a;
    --band-blue: #1c6cc0;
    --green: #8cc540;
    --green-dark: #6fa62a;
    --orange: #f39a1e;
    --text: #555;
    --muted: #888;
    --white: #fff;
    --footer-bottom: #7ab232;
  }
  * { box-sizing: border-box; margin: 0; padding: 0; }
  html, body { width: 789px; height: 1200px; overflow: hidden; }
  body { font-family: "Open Sans", Arial, sans-serif; color: var(--text); background: var(--white); position: relative; }

  .site-header { height: 48px; display: flex; align-items: stretch; justify-content: space-between; padding-left: 44px; background: var(--white); }
  .brand { display: flex; align-items: center; gap: 7px; font-weight: 700; font-size: 19px; color: var(--blue); }
  .brand-dot { width: 16px; height: 16px; border-radius: 50%; background: var(--green); }
  .main-nav { display: flex; align-items: stretch; background: var(--blue); padding: 0 28px 0 18px; margin-right: 29px; }
  .main-nav a { display: flex; align-items: center; padding: 0 10px; color: var(--white); text-decoration: none; font-size: 8.5px; font-weight: 600; letter-spacing: .3px; }
  .main-nav a.active { background: var(--blue-dark); }

  .hero { position: relative; height: 350px; overflow: hidden; }
  .hero-image { position: absolute; inset: 0; background: radial-gradient(ellipse at 72% 45%, #6d7683 0%, #3a414c 45%, #1f252e 100%); }
  .hero-copy { position: absolute; left: 58px; top: 140px; color: var(--white); font-size: 21px; font-weight: 300; line-height: 1.3; }
  .hero-copy strong { font-weight: 600; }
  .hero-arrow { position: absolute; top: 158px; width: 14px; height: 26px; }
  .hero-arrow.prev { left: 14px; }
  .hero-arrow.next { right: 14px; }
  .hero-dots { position: absolute; left: 105px; bottom: 28px; display: flex; gap: 5px; }
  .hero-dots span { width: 7px; height: 7px; border-radius: 50%; background: rgba(255,255,255,.55); }
  .hero-dots span.on { background: var(--white); }

  .services { height: 247px; text-align: center; padding-top: 18px; }
  .section-title { color: var(--blue); font-size: 14px; font-weight: 600; text-transform: uppercase; }
  .section-sub { font-size: 8.5px; color: var(--muted); margin-top: 3px; }
  .service-grid { display: flex; justify-content: center; gap: 24px; margin-top: 20px; padding: 0 40px; }
  .service { width: 160px; }
  .service-icon { width: 54px; height: 54px; margin: 0 auto 10px; }
  .service h3 { font-size: 11px; font-weight: 600; color: #444; margin-bottom: 5px; }
  .service p { font-size: 7.5px; line-height: 1.5; color: var(--muted); }

  .experience { height: 223px; background: linear-gradient(180deg, #2476c9, var(--band-blue) 60%, #1a62ae); color: var(--white); text-align: center; padding: 22px 70px 0; }
  .experience-icon { width: 30px; height: 30px; margin: 0 auto 8px; }
  .experience h2 { font-size: 16px; font-weight: 600; margin-bottom: 10px; }
  .experience .lead { font-size: 8.5px; font-weight: 700; line-height: 1.45; margin-bottom: 10px; }
  .experience p { font-size: 8.5px; line-height: 1.55; }

  .welcome { height: 152px; text-align: center; padding: 14px 80px 0; }
  .welcome h2 { color: var(--blue); font-size: 14px; font-weight: 600; margin-bottom: 6px; }
  .welcome p { font-size: 8px; line-height: 1.55; color: var(--muted); }
  .btn { display: inline-block; margin-top: 14px; background: var(--green); color: var(--white); font-size: 8px; font-weight: 700; padding: 6px 14px; text-decoration: none; border-radius: 2px; }

  .site-footer { height: 155px; background: var(--green); display: flex; padding: 14px 0 0 44px; gap: 0; color: var(--white); }
  .footer-col { width: 140px; }
  .footer-col h4 { font-size: 8.5px; font-weight: 700; margin-bottom: 6px; }
  .footer-col li { list-style: none; font-size: 7.5px; line-height: 1.6; }
  .social li { display: flex; align-items: center; gap: 5px; }
  .social li::before { content: ""; width: 8px; height: 8px; background: rgba(255,255,255,.85); }
  .footer-bottom { height: 25px; background: var(--footer-bottom); color: var(--white); font-size: 7px; display: flex; align-items: center; justify-content: center; }
</style>
</head>
<body>
<header class="site-header">
  <div class="brand"><span class="brand-dot"></span>TallowMere</div>
  <nav class="main-nav">
    <a class="active" href="#">HOME</a><a href="#">PRODUCTS</a><a href="#">SERVICES</a><a href="#">RESOURCES</a><a href="#">BLOG</a><a href="#">ABOUT US</a><a href="#">CONTACT US</a>
  </nav>
</header>

<section class="hero">
  <div class="hero-image" role="img" aria-label="Businessman in a suit holding a black umbrella under a stormy sky"></div>
  <div class="hero-copy">Helping Businesses <strong>THRIVE</strong><br>by turning every transaction<br>into a relationship.</div>
  <svg class="hero-arrow prev" viewBox="0 0 14 26"><path d="M12 2 2 13l10 11" fill="none" stroke="#fff" stroke-width="2.5"/></svg>
  <svg class="hero-arrow next" viewBox="0 0 14 26"><path d="M2 2l10 11L2 24" fill="none" stroke="#fff" stroke-width="2.5"/></svg>
  <div class="hero-dots"><span class="on"></span><span></span><span></span><span></span><span></span></div>
</section>

<section class="services">
  <h2 class="section-title">Our Services</h2>
  <p class="section-sub">When marketing your business, nothing you do is outside the reach of social media</p>
  <div class="service-grid">
    <div class="service">
      <svg class="service-icon" viewBox="0 0 54 54"><circle cx="27" cy="27" r="25" fill="#eaf2fb" stroke="var(--blue)" stroke-width="2"/><path d="M17 27h18m-6-6 6 6-6 6" fill="none" stroke="var(--blue)" stroke-width="2.5"/></svg>
      <h3>Inbound Marketing</h3>
      <p>Today's buyers are in control of how they find your company and what they learn before they ever call.</p>
    </div>
    <div class="service">
      <svg class="service-icon" viewBox="0 0 54 54"><circle cx="27" cy="27" r="25" fill="#eaf2fb" stroke="var(--blue)" stroke-width="2"/><path d="M37 27H19m6-6-6 6 6 6" fill="none" stroke="var(--blue)" stroke-width="2.5"/></svg>
      <h3>Outbound Marketing</h3>
      <p>Outbound marketing still proves to be a strong way to reach new riders and grow loyal accounts.</p>
    </div>
    <div class="service">
      <svg class="service-icon" viewBox="0 0 54 54"><circle cx="27" cy="27" r="25" fill="#eaf2fb" stroke="var(--blue)" stroke-width="2"/><rect x="16" y="18" width="22" height="15" rx="3" fill="none" stroke="var(--blue)" stroke-width="2.5"/><path d="M21 33l-2 5 7-5" fill="var(--blue)"/></svg>
      <h3>Social Media Marketing</h3>
      <p>As leading specialists in limousine and chauffeured transport marketing, we keep you in the conversation.</p>
    </div>
    <div class="service">
      <svg class="service-icon" viewBox="0 0 54 54"><circle cx="27" cy="27" r="25" fill="#eaf2fb" stroke="var(--blue)" stroke-width="2"/><rect x="20" y="14" width="14" height="26" rx="2" fill="none" stroke="var(--blue)" stroke-width="2.5"/><circle cx="27" cy="36" r="1.5" fill="var(--blue)"/></svg>
      <h3>Mobile Marketing</h3>
      <p>More people now book rides from a phone, so your brand must look sharp on every small screen.</p>
    </div>
  </div>
</section>

<section class="experience">
  <svg class="experience-icon" viewBox="0 0 30 30"><rect width="30" height="30" rx="3" fill="var(--orange)"/><rect x="7" y="11" width="16" height="11" rx="1.5" fill="#fff"/><path d="M12 11V8.5h6V11" fill="none" stroke="#fff" stroke-width="1.8"/></svg>
  <h2>You're In the Experience Business</h2>
  <p class="lead">If you're competitor focused, you have to wait until there is a competitor doing something. Being customer-focused allows you to be more pioneering." Nine words from Northvale.com's Harlan Dovecote.</p>
  <p>Like Northvale.com, our top limousine and corporate ground transportation clients are industry pioneers and success stories. They are the companies that are changing the chauffeured transportation experience. TallowMere's clients provide quality service, make the best use of their resources and are authentic in their messaging. Their customers are excited about their companies, their people and their services. Sometimes, they'll even pay them a little bit more.</p>
</section>

<section class="welcome">
  <h2>Welcome to our site</h2>
  <p>We are a Fan Factory. We create opportunities for people to get excited about your company, which drives the creation of transactional value for your business. We create Fans – not just page likes, but people who pay attention to you and spend more money with you.</p>
  <p>TallowMere and our clients dare to be different. We create campaigns in which our clients stand out from the crowd in fun, obvious ways so they are never seen as a "me too" in the industry. We help you rise above the "sea of sameness" by not only moving the needle but changing the game, so you can achieve a wide array of strategic marketing victories, both on and off line. The TallowMere Fan Factory improves their visibility, builds market share and increases bookings both on and off line.</p>
  <a class="btn" href="#">READ MORE</a>
</section>

<footer class="site-footer">
  <div class="footer-col"><h4>Home</h4><ul><li>Home</li><li>Products</li><li>Services</li><li>Resources</li><li>Blog</li><li>About us</li><li>Contact Us</li></ul></div>
  <div class="footer-col"><h4>Services</h4><ul><li>Customer Retention &amp; Loyalty</li><li>Support to Increase the Sale</li><li>Online Image &amp; Reputation</li><li>Management/Online Marketing</li><li>Social Media Marketing</li><li>Outbound Marketing</li><li>Inbound Marketing</li></ul></div>
  <div class="footer-col"><h4>Links</h4><ul><li>Terms and Conditions</li><li>Privacy Policy</li></ul></div>
  <div class="footer-col social"><h4>Social Media</h4><ul><li>Chatterfold</li><li>Birdline</li><li>Linkwise</li><li>Orbitplus</li></ul></div>
  <div class="footer-col"><h4>Contact Information</h4><ul><li>Toll Free Phone: 800-555-0142</li><li>E-mail: info@tallowmere.com</li></ul></div>
</footer>
<div class="footer-bottom">© 2014 TallowMere. All rights reserved.</div>
</body>
</html>
```